Equipment financing with a focus on truck financing, need a business card

Looking to get a business card designed that stands out to represent my financing company. Vornel Truck & Equipment Financing. Even though I can finance all types of equipment my main focus will be on trucks. I can do financing all across Canada.I liked the design on the one I attached for Tessmark Holdings Corp.I want a truck picture to be on the card like the Brisko Lending card (this is not my company, it is someone elses and I've attached it as a sample) . If you can add a construction piece of equipment as well that would be great, something along the lines of the attachment for Brisko Lending. I want the Khanda symbol as well on the card, it can be one color if you choose, I thought something like the attachment stood out more. The Khanda is a symbol of Sikh faith. I am targeting most of my business to Sikh truck drivers. Card should have a black background so it stands out. It can be horizontal or vertical or a combination of both.Thinking the front of the card has a larger Khanda symbol and then a smaller one inside of it and then my name Vornel Truck & Equipment Financing .
Target Market(s)
Deal with people in all types of industries
Industry/Entity Type
Finance
Contact Information for Business Card
The front could be split black and other colors to make the khanda and lettering pop out. Open to any type of design.
Back of card would say
President
Derek Mowat
Mobile
403 555 0172
Email
Derek.Vornelli@quillbrookfunding.com
at the bottom like the Tessmark Holdings Corp card I want it to say and stand out
EQUIPMENT FINANCE SPECIALIST
am open to anything that looks great and stands out, modern and bold.
Colors
Designer to choose colors to be used in the design.
Requirements
Must have
- I would like the color of the khanda symbol to be similar to the picture I attached, kind of a goldish color, make the letters in a similar color as well
- - Modern
- - Different
- - Stand Out
- - Makes an Impression
Nice to have
- In summary, Brisko Lending is not my logo nor my business name its. I would like something similar though with a truck on the card, and if there is a way perhaps a piece of construction equipment.
- VORNEL TRUCK & EQUIPMENT FINANCING is the name of my company.
- I want a card that stands out and is bold like the Tessmark Holdings Corp card I attached
- The Khanda is a sikh symbol, I attached a pic of what it looks like.

```html
<!DOCTYPE html>
<html lang="en">
<head>
<meta charset="utf-8">
<title>Vornel Truck &amp; Equipment Financing — Business Card</title>
<link rel="stylesheet" href="https://fonts.googleapis.com/css2?family=Open+Sans:wght@400;600&family=Crimson+Text:ital@1&display=swap">
<style>
  :root {
    --backdrop: #2a2a2a;
    --card: #121212;
    --card-edge: #1c1c1c;
    --accent: #f0841e;
    --ink: #e9e9e9;
    --ink-soft: #cfcfcf;
  }
  * { box-sizing: border-box; margin: 0; padding: 0; }
  html, body { width: 1200px; height: 716px; overflow: hidden; }
  body {
    background: var(--backdrop);
    font-family: "Open Sans", Arial, sans-serif;
    display: flex;
    align-items: center;
    justify-content: center;
    gap: 48px;
  }
  .card {
    position: relative;
    width: 525px;
    height: 300px;
    background: var(--card);
    border: 1px solid var(--card-edge);
    border-radius: 18px;
    overflow: hidden;
  }

  /* Front */
  .card--front .brand {
    position: absolute;
    left: 62px;
    top: 82px;
    display: flex;
    align-items: center;
    gap: 14px;
  }
  .brand-dot {
    flex: none;
    width: 62px; height: 62px;
    border-radius: 50%;
    border: 5px solid var(--accent);
  }
  .brand-name {
    font-size: 60px;
    font-weight: 600;
    color: var(--ink);
    letter-spacing: 1px;
    line-height: 1;
  }
  .card--front .brand-tagline {
    position: absolute;
    left: 140px;
    top: 150px;
    font-size: 14px;
    color: var(--accent);
    letter-spacing: 0.5px;
  }
  .specialty {
    position: absolute;
    left: 0; right: 0;
    top: 212px;
    text-align: center;
    font-size: 18px;
    color: var(--accent);
    letter-spacing: 0.5px;
  }

  /* Back */
  .person-marker {
    position: absolute;
    left: 44px; top: 46px;
    width: 40px; height: 40px;
    background: var(--accent);
    border-radius: 50%;
  }
  .person { position: absolute; left: 100px; top: 48px; }
  .person-name {
    font-size: 22px;
    color: var(--ink);
    letter-spacing: 0.5px;
  }
  .person-role {
    font-family: "Crimson Text", Georgia, serif;
    font-style: italic;
    font-size: 15px;
    color: var(--accent);
    margin-top: -2px;
  }
  .contact { position: absolute; left: 46px; top: 118px; list-style: none; }
  .contact li {
    display: flex;
    align-items: center;
    gap: 10px;
    font-size: 14px;
    color: var(--ink-soft);
    margin-bottom: 8px;
  }
  .contact svg { width: 13px; height: 13px; fill: var(--accent); }

  .card--back .brand-vertical {
    position: absolute;
    right: 18px;
    bottom: 18px;
    width: 260px;
    height: 90px;
    transform-origin: bottom right;
    transform: rotate(-90deg) translateX(260px);
  }
  .brand-vertical .brand {
    display: flex; align-items: center; gap: 10px;
  }
  .brand-vertical .brand-dot { width: 52px; height: 52px; border-width: 4px; }
  .brand-vertical .brand-name { font-size: 46px; }
  .brand-vertical .brand-tagline {
    font-size: 11px;
    color: var(--accent);
    margin-left: 64px;
    letter-spacing: 0.4px;
  }
</style>
</head>
<body>
  <section class="card card--front" aria-label="Card front">
    <div class="brand">
      <span class="brand-dot" aria-hidden="true"></span>
      <span class="brand-name">VORNEL</span>
    </div>
    <p class="brand-tagline">TRUCK &amp; EQUIPMENT FINANCING</p>
    <p class="specialty">EQUIPMENT FINANCE SPECIALIST</p>
  </section>

  <section class="card card--back" aria-label="Card back">
    <span class="person-marker" aria-hidden="true"></span>
    <div class="person">
      <p class="person-name">DEREK MOWAT</p>
      <p class="person-role">President</p>
    </div>
    <ul class="contact">
      <li>
        <svg viewBox="0 0 24 24" aria-hidden="true"><path d="M6.6 10.8a15 15 0 0 0 6.6 6.6l2.2-2.2c.3-.3.7-.4 1-.2 1.1.4 2.3.6 3.6.6.6 0 1 .4 1 1V20c0 .6-.4 1-1 1A17 17 0 0 1 3 4c0-.6.4-1 1-1h3.5c.6 0 1 .4 1 1 0 1.3.2 2.5.6 3.6.1.3 0 .7-.2 1z"/></svg>
        403 555 0172
      </li>
      <li>
        <svg viewBox="0 0 24 24" aria-hidden="true"><path d="M2 5h20v14H2z M2 5l10 7 10-7" stroke="#121212" stroke-width="1.5"/></svg>
        Derek.Vornelli@quillbrookfunding.com
      </li>
    </ul>
    <div class="brand-vertical">
      <div class="brand">
        <span class="brand-dot" aria-hidden="true"></span>
        <span class="brand-name">VORNEL</span>
      </div>
      <p class="brand-tagline">TRUCK &amp; EQUIPMENT FINANCING</p>
    </div>
  </section>
</body>
</html>
```